We are a doctors medical practice
I need the business card to be eye catching and memorable,
to reflect professionalism, yet also warmth and care

the numbers need to be easy to see, for the elderly

and the logo also in a location that is large enough to see and be eye catching

Back of card:
opening hours:
Mon- Fri 8.30am to 6pm
Sat 9am to 4pm

rows for appontments, date and time
Updates

HiĀ 

Modification to company name

BRAMBLEWOOD HOME HEALTH MEDICAL PRACTICE

Thanks
Clara

Reason: I am look for a unique design that also fulfils the design brief

I have attempted to post a .eps and .ai file of the logo

Target Market(s)

needs to appeal to the majority, mainly adults

Industry/Entity Type

Medical

Contact Information for Business Card

company name: Bramblewood Home Health Medical Practice
Name: Dr Clara Ostrowski-Vey
Qualifications: MBBS, Bsci(med), FRACGP, DCH, SH&FPA, Dip Derm
Address: Shop 3/41-43 Calder Rd, Brookvale 2371
Ph: 02 9418 3052
Fax: 02 9436 8120

Requirements
Nice to have
• I like balance
gold/ silver incorporated, as well as the other colours in the logo- but not limited to these colours
a "medical" feel
Should not have
• dark or strong colours

```html
<!DOCTYPE html>
<html lang="en">
<head>
<meta charset="utf-8">
<title>Bramblewood Home Health Medical Practice – Business Card</title>
<link href="https://fonts.googleapis.com/css2?family=Open+Sans:wght@400;600;700;800&display=swap" rel="stylesheet">
<style>
  :root {
    --page-bg: #e9edef;
    --card-white: #ffffff;
    --silver: #dcdcdc;
    --silver-dark: #c4c4c4;
    --brand-blue: #1a6fc4;
    --band-blue: #1b86cf;
    --text-grey: #7a7a7a;
    --text-dark: #2c2c2c;
    --leaf-green: #a6c93a;
    --gold: #f0912a;
    --dots: #555555;
  }
  * { box-sizing: border-box; margin: 0; padding: 0; }
  html, body {
    width: 1200px; height: 900px; overflow: hidden;
    background: var(--page-bg);
    font-family: "Open Sans", Arial, sans-serif;
  }
  .card {
    position: absolute; width: 560px; height: 320px; left: 320px;
    background: var(--card-white);
    box-shadow: 0 6px 18px rgba(0,0,0,.18);
    overflow: hidden;
  }
  .card-front { top: 80px; }
  .card-back { top: 500px; background: #f7f7f7; }
  .card-art { position: absolute; inset: 0; width: 100%; height: 100%; }

  /* Front */
  .doctor { position: absolute; left: 20px; top: 16px; }
  .doctor-name { color: var(--brand-blue); font-weight: 800; font-size: 23px; }
  .doctor-quals { color: var(--text-grey); font-size: 13.5px; line-height: 1.35; margin-top: 4px; }
  .brand-mark {
    position: absolute; right: 22px; top: 22px; width: 118px; height: 118px;
    border: 5px solid var(--brand-blue); border-radius: 50%;
    display: flex; align-items: center; justify-content: center;
  }
  .brand-mark span { color: var(--brand-blue); font-weight: 700; font-size: 14px; }
  .practice-name {
    position: absolute; left: 18px; top: 150px;
    color: var(--brand-blue); font-weight: 800; font-size: 17.5px; letter-spacing: .2px;
  }
  .contact-list { position: absolute; right: 26px; top: 196px; list-style: none; }
  .contact-list li {
    display: flex; align-items: center; gap: 8px;
    color: var(--text-dark); font-weight: 600; font-size: 17px; line-height: 28px;
  }
  .contact-list svg { width: 20px; height: 20px; }
  .address {
    position: absolute; right: 26px; bottom: 18px;
    color: var(--text-dark); font-weight: 600; font-size: 17px;
  }

  /* Back */
  .hours-band {
    position: absolute; left: 0; top: 0; bottom: 0; width: 58px;
    background: var(--band-blue); color: #fff;
    display: flex; align-items: center; justify-content: center;
  }
  .hours-text {
    writing-mode: vertical-rl; transform: rotate(180deg);
    font-size: 12.5px; font-weight: 600; text-align: center; line-height: 1.3;
  }
  .hours-text strong { font-weight: 800; }
  .faint-mark {
    position: absolute; left: 235px; top: 70px; width: 200px; height: 200px;
    border: 10px solid rgba(27,134,207,.12); border-radius: 50%;
    display: flex; align-items: center; justify-content: center;
  }
  .faint-mark span { color: rgba(27,134,207,.18); font-weight: 700; font-size: 20px; }
  .appointments { position: absolute; left: 76px; right: 18px; top: 14px; }
  .appointments-head {
    display: flex; justify-content: space-between;
    color: var(--text-dark); font-weight: 700; font-size: 13px; margin-bottom: 8px;
  }
  .appointments-head span:last-child { padding-right: 14px; }
  .appointment-row { height: 25px; border-bottom: 1.5px dotted var(--dots); }
</style>
</head>
<body>

<section class="card card-front" aria-label="Business card front">
  <svg class="card-art" viewBox="0 0 560 320" preserveAspectRatio="none" aria-hidden="true">
    <defs>
      <linearGradient id="silverFade" x1="0" y1="0" x2="1" y2="1">
        <stop offset="0" stop-color="#d3d3d3"/>
        <stop offset="1" stop-color="#f2f2f2"/>
      </linearGradient>
    </defs>
    <path d="M0 0 H560 V8 C420 40 240 90 0 112 Z" fill="url(#silverFade)"/>
    <path d="M0 112 C240 90 420 40 560 8" fill="none" stroke="var(--gold)" stroke-width="5"/>
    <path d="M0 124 C240 102 420 52 560 20" fill="none" stroke="var(--gold)" stroke-width="1.5" opacity=".7"/>
    <path d="M0 320 C160 270 360 200 560 150 V320 Z" fill="var(--leaf-green)"/>
    <path d="M0 316 C160 266 360 196 560 146" fill="none" stroke="var(--gold)" stroke-width="4"/>
  </svg>

  <div class="doctor">
    <h1 class="doctor-name">Dr Clara Ostrowski-Vey</h1>
    <p class="doctor-quals">MBBS, Bsci(med), FRACGP,<br>DCH, SH&amp;FPA, Dip Derm</p>
  </div>

  <div class="brand-mark"><span>Bramblewood</span></div>

  <h2 class="practice-name">BRAMBLEWOOD HOME HEALTH MEDICAL PRACTICE</h2>

  <ul class="contact-list">
    <li>
      <svg viewBox="0 0 20 20" aria-label="Phone"><path d="M3 7 Q10 2 17 7 V9 H13 V7 H7 V9 H3 Z" fill="#222"/><rect x="4" y="10" width="12" height="7" rx="1.5" fill="#222"/><circle cx="10" cy="13.5" r="2" fill="#ddd"/></svg>
      02 9418 3052
    </li>
    <li>
      <svg viewBox="0 0 20 20" aria-label="Fax"><rect x="3" y="2" width="14" height="16" rx="1.5" fill="none" stroke="#222" stroke-width="1.8"/><rect x="6" y="5" width="8" height="4" fill="#222"/><path d="M6 12h2M9 12h2M12 12h2M6 15h2M9 15h2M12 15h2" stroke="#222" stroke-width="1.6"/></svg>
      02 9436 8120
    </li>
  </ul>

  <p class="address">Shop 3/41-43 Calder Rd, Brookvale 2371</p>
</section>

<section class="card card-back" aria-label="Business card back">
  <div class="hours-band">
    <p class="hours-text"><strong>OPENING HOURS:</strong> Mon- Fri 8.30am to 6pm<br>Sat 9am to 4pm</p>
  </div>

  <div class="faint-mark" aria-hidden="true"><span>Bramblewood</span></div>

  <div class="appointments">
    <div class="appointments-head"><span>Appontments</span><span>Date &amp; Time</span></div>
    <div class="appointment-row"></div>
    <div class="appointment-row"></div>
    <div class="appointment-row"></div>
    <div class="appointment-row"></div>
    <div class="appointment-row"></div>
    <div class="appointment-row"></div>
    <div class="appointment-row"></div>
    <div class="appointment-row"></div>
    <div class="appointment-row"></div>
    <div class="appointment-row"></div>
    <div class="appointment-row"></div>
  </div>
</section>

</body>
</html>
```